W.I.Q 'Wadi Ibn Qutub' for General Transportation

this company is a Iraqi based company.
It provides a number of logistics activities such as;
Overland Transportation
High and heavy logistics
Customs clearance
warehousing
Automotive logistics
The company has been registered since 2009.
If you have any other questions please feel free to ask.
Target Market(s)
Automotive
White goods
All Trading sectors
Industry/Entity Type
Automotive

```html
<!DOCTYPE html>
<html lang="en">
<head>
<meta charset="utf-8">
<title>Wadi Ibn Qutub Transportation</title>
<link href="https://fonts.googleapis.com/css2?family=Ubuntu:wght@300;400;500;700&family=Arimo:wght@400&display=swap" rel="stylesheet">
<style>
:root{
  --navy:#13305f;
  --blue:#2a5ca8;
  --link:#3e5f8e;
  --text:#555b63;
  --muted:#777;
  --page:#f5f7f9;
  --footer:#3d3d3d;
  --footer-bottom:#2b2b2b;
  --footer-text:#a9a9a9;
  --card-bar:#6a6a6a;
}
*{margin:0;padding:0;box-sizing:border-box}
html,body{width:1024px;height:1200px;overflow:hidden}
body{position:relative;background:var(--page);font-family:'Ubuntu',sans-serif;color:var(--text)}

.site-header{position:absolute;left:0;top:0;width:1024px;height:61px;background:linear-gradient(#fafafa,#e9e9e9);border-bottom:1px solid #d2d2d2;z-index:2}
.brand{position:absolute;left:135px;top:14px;display:flex;align-items:center;gap:16px}
.brand-mark{font-weight:700;font-size:30px;color:var(--navy);letter-spacing:1px;line-height:1}
.brand-name{font-size:15px;font-weight:400;color:var(--navy);line-height:1.1}
.brand-name span{display:block;color:#8a8f96;font-weight:300;font-size:16px}
.main-nav a{position:absolute;top:27px;font-size:12px;color:#333;text-decoration:none}
.main-nav a.active{color:var(--blue)}
.main-nav .indicator{position:absolute;left:465px;top:0;width:34px;height:3px;background:var(--navy)}
.call{position:absolute;left:776px;top:22px}
.call-text{position:absolute;left:28px;top:-1px;white-space:nowrap}
.call-text small{display:block;font-size:9px;color:#888;letter-spacing:.3px}
.call-text b{display:block;font-size:11px;color:var(--navy);font-weight:700}

.hero{position:absolute;left:0;top:61px;width:1024px;height:528px;background:linear-gradient(160deg,#5e6f86 0%,#a07a45 35%,#c99a5a 55%,#8d98a8 80%,#dcdcdc 100%)}
.hero-caption{position:absolute;left:540px;top:179px;width:484px;height:131px;background:rgba(3,15,35,.85);padding:25px 0 0 41px;color:#fff}
.hero-caption h1{font-weight:400;font-size:27px;line-height:34px}
.hero-caption p{font-size:13.5px;margin-top:7px;font-weight:300}

.fade{position:absolute;left:0;top:589px;width:1024px;height:120px;background:linear-gradient(#dfe2e6,var(--page))}

.service-card{position:absolute;top:524px;width:177px;height:229px;background:#fff;box-shadow:0 1px 3px rgba(0,0,0,.18)}
.service-card.first::before{content:"";position:absolute;left:0;top:-5px;width:100%;height:5px;background:var(--card-bar)}
.service-card h2{font-size:11.5px;font-weight:500;color:var(--navy);text-align:center;margin-top:20px;line-height:14px}
.service-card .thumb{margin:14px 0 0 14px;width:149px;height:78px}
.service-card p{font-family:'Arimo',sans-serif;font-size:7.5px;line-height:11px;color:#666;margin:20px 14px 0 14px}
.service-card a{position:absolute;left:14px;top:196px;font-size:8px;font-weight:700;color:var(--link)}

.section-title{position:absolute;top:824px;font-size:14px;font-weight:500;color:var(--navy)}
.welcome-img{position:absolute;left:136px;top:859px;width:112px;height:87px;background:linear-gradient(#6b5a3f,#c09358 60%,#d8d8d8)}
.welcome-text{position:absolute;left:266px;top:855px;width:240px;font-size:10.5px;line-height:16px;color:var(--text)}
.reasons{position:absolute;left:527px;top:859px;list-style:none}
.reasons li{position:relative;padding-left:26px;height:27.2px;font-size:10.5px;color:var(--text);line-height:16px}
.reasons svg{position:absolute;left:1px;top:1px}

.site-footer{position:absolute;left:0;top:1019px;width:1024px;height:147px;background:var(--footer);border-top:2px solid #555}
.footer-mark{position:absolute;left:168px;top:50px;font-size:34px;font-weight:700;color:#7c7c7c;letter-spacing:1px}
.footer-col{position:absolute;top:26px}
.footer-col h3{font-size:12px;font-weight:500;color:#fff;margin-bottom:9px}
.footer-col ul{list-style:none}
.footer-col li{font-family:'Arimo',sans-serif;font-size:8.5px;color:var(--footer-text);height:19.2px;padding-left:10px;position:relative}
.footer-col li::before{content:"";position:absolute;left:0;top:2px;border-left:3px solid #888;border-top:3px solid transparent;border-bottom:3px solid transparent}
.footer-col li.current{color:#3b8fe0}
.contact-list li{padding-left:20px;height:24px}
.contact-list li::before{display:none}
.contact-list svg{position:absolute;left:0;top:0}
.social{display:flex;gap:8px}
.social span{width:28px;height:28px;border-radius:2px;box-shadow:0 1px 2px rgba(0,0,0,.4)}
.footer-bottom{position:absolute;left:0;top:1166px;width:1024px;height:34px;background:var(--footer-bottom);font-family:'Arimo',sans-serif;font-size:8.5px;color:var(--footer-text)}
.footer-bottom .copy{position:absolute;left:134px;top:12px}
.footer-bottom .legal{position:absolute;left:786px;top:12px}
</style>
</head>
<body>

<header class="site-header">
  <div class="brand">
    <div class="brand-mark">W.I.Q</div>
    <div class="brand-name">Wadi Ibn Qutub<span>Transportation</span></div>
  </div>
  <nav class="main-nav">
    <span class="indicator"></span>
    <a class="active" style="left:468px" href="#">Home</a>
    <a style="left:534px" href="#">Services</a>
    <a style="left:617px" href="#">About</a>
    <a style="left:685px" href="#">Contact</a>
  </nav>
  <div class="call">
    <svg width="19" height="19" viewBox="0 0 19 19"><rect width="19" height="19" rx="3" fill="#13305f"/><path d="M6 4.5l2 0 1 3-1.3 1a6 6 0 0 0 3 3l1-1.3 3 1v2c0 .6-.5 1-1 1A9.5 9.5 0 0 1 5 5.5c0-.6.4-1 1-1z" fill="#fff"/></svg>
    <div class="call-text"><small>CALL US TODAY</small><b>1800.555.0142</b></div>
  </div>
</header>

<section class="hero" role="img" aria-label="Warehouse interior with an orange forklift lifting a pallet of cardboard boxes between blue racks">
  <div class="hero-caption">
    <h1>We provide the highest<br>quality of service you need.</h1>
    <p>Lorem ipsum dolor sit amet, consectetur adipisicing</p>
  </div>
</section>
<div class="fade"></div>

<article class="service-card first" style="left:135px">
  <h2>Overland Transportation</h2>
  <div class="thumb" role="img" aria-label="White truck driving on an open road" style="background:linear-gradient(#6e93c6,#cdd9e6 55%,#6b6650)"></div>
  <p>Lorem ipsum dolor sit amet, consectetur adipisicing elit, sed do eiusmod tempor incididunt ut labore .</p>
  <a href="#">READ MORE</a>
</article>
<article class="service-card" style="left:327px">
  <h2>High and Heavy Logistics</h2>
  <div class="thumb" role="img" aria-label="Worker in safety gear beside a shipping container at a port" style="background:linear-gradient(90deg,#2c4f86,#5c7fb0 50%,#c8ccd6)"></div>
  <p>Lorem ipsum dolor sit amet, consectetur adipisicing elit, sed do eiusmod tempor incididunt ut labore .</p>
  <a href="#">READ MORE</a>
</article>
<article class="service-card" style="left:519px">
  <h2>Customs Clearance</h2>
  <div class="thumb" role="img" aria-label="Empty warehouse hall with tall windows" style="background:linear-gradient(#7a6233,#c8a86a 50%,#4d3d24)"></div>
  <p>Lorem ipsum dolor sit amet, consectetur adipisicing elit, sed do eiusmod tempor incididunt ut labore .</p>
  <a href="#">READ MORE</a>
</article>
<article class="service-card" style="left:711px">
  <h2>Automotive Logistics</h2>
  <div class="thumb" role="img" aria-label="Workers loading cardboard boxes into a delivery van" style="background:linear-gradient(90deg,#4a3f35,#9a8a76 50%,#d6b892)"></div>
  <p>Lorem ipsum dolor sit amet, consectetur adipisicing elit, sed do eiusmod tempor incididunt ut labore .</p>
  <a href="#">READ MORE</a>
</article>

<h2 class="section-title" style="left:136px">Welcome to Wadi Ibn Qutub Transporation</h2>
<div class="welcome-img" role="img" aria-label="Forklift in a warehouse aisle"></div>
<p class="welcome-text">It is a long established fact that a reader will be distracted by the readable content of a page when looking at its layout. The point of using Lorem Ipsum is that it has a more-or-less normal distribution of letters, as opposed to using 'Content here, content here', making it look like.</p>

<h2 class="section-title" style="left:527px">Why Choose Us?</h2>
<ul class="reasons">
  <li><svg width="14" height="14" viewBox="0 0 14 14"><circle cx="7" cy="7" r="7" fill="#8a8a8a"/><path d="M6 4l3 3-3 3" stroke="#fff" stroke-width="1.5" fill="none"/></svg>Cras rutrum leo at odio volutpat id blandit fugiats ipsum ornare.</li>
  <li><svg width="14" height="14" viewBox="0 0 14 14"><circle cx="7" cy="7" r="7" fill="#8a8a8a"/><path d="M6 4l3 3-3 3" stroke="#fff" stroke-width="1.5" fill="none"/></svg>Donec fermentum porttitor nunc, sit amet gravida est porttitor vel.</li>
  <li><svg width="14" height="14" viewBox="0 0 14 14"><circle cx="7" cy="7" r="7" fill="#8a8a8a"/><path d="M6 4l3 3-3 3" stroke="#fff" stroke-width="1.5" fill="none"/></svg>Maecenas quis nisi in uctus adipiscing sed vehicula tellus amet dolore.</li>
  <li><svg width="14" height="14" viewBox="0 0 14 14"><circle cx="7" cy="7" r="7" fill="#8a8a8a"/><path d="M6 4l3 3-3 3" stroke="#fff" stroke-width="1.5" fill="none"/></svg>Aenean faucibus sapien a odio varius aliquet voluptas sadips..</li>
</ul>

<footer class="site-footer">
  <div class="footer-mark">W.I.Q</div>
  <div class="footer-col" style="left:329px">
    <h3>Navigation</h3>
    <ul><li>Home</li><li>About</li><li>Services</li><li>Contact</li></ul>
  </div>
  <div class="footer-col" style="left:457px">
    <h3>Services</h3>
    <ul><li class="current">Menu1</li><li>Menu1</li><li>Menu1</li><li>Menu1</li></ul>
  </div>
  <div class="footer-col" style="left:585px">
    <h3>Contact Us</h3>
    <ul class="contact-list">
      <li><svg width="10" height="10" viewBox="0 0 10 10"><path d="M1.5 .5h2l1 2.5-1.2 1a5 5 0 0 0 2.7 2.7l1-1.2 2.5 1v2c0 .5-.4 1-1 1A8.5 8.5 0 0 1 .5 1.5c0-.6.4-1 1-1z" fill="#999"/></svg>+1800-555-0142</li>
      <li><svg width="11" height="8" viewBox="0 0 11 8"><rect width="11" height="8" fill="#999"/><path d="M0 0l5.5 4.5L11 0" stroke="#3d3d3d" fill="none"/></svg>info@wadiibnqutub.example</li>
      <li><svg width="8" height="11" viewBox="0 0 8 11"><path d="M4 0a4 4 0 0 1 4 4c0 3-4 7-4 7S0 7 0 4a4 4 0 0 1 4-4z" fill="#999"/><circle cx="4" cy="4" r="1.4" fill="#3d3d3d"/></svg>Your Address, Your Country<br><br>Your Zip Code</li>
    </ul>
  </div>
  <div class="footer-col" style="left:758px">
    <h3>Social</h3>
    <div class="social">
      <span style="background:#3b5b9a"></span>
      <span style="background:#2fa3db"></span>
      <span style="background:#1a6fa5"></span>
      <span style="background:#d2382b"></span>
    </div>
  </div>
</footer>
<div class="footer-bottom">
  <span class="copy">Copyright 2014 © CompanyName - All Rights Reserved</span>
  <span class="legal">Site Map &nbsp;&nbsp;•&nbsp;&nbsp; Privacy Policy</span>
</div>

</body>
</html>
```